Bref créative
Stationary Project
BRQ - Bright Rivers Quality
Simple
Dale Morrow
Toms River, NJ
dmorrow@br-quality.example
brightriversquality.example
Industry Type is for Photography. For some reason it does not show when I confirm brief. Add "Bringing Nature Indoors" to project. This font style can be different than the BRQ Logo Font. (possibly script, but must be crisp and clear). Can use color but must not distract from Falcon Image. Also at this point in time, name, email, etc should be in the same font as the Logo but may possibly be changed once designs are submitted and reviewed by my staff.

```html
<!DOCTYPE html>
<html lang="en">
<head>
<meta charset="utf-8">
<title>BRQ - Bright Rivers Quality — Stationery</title>
<link rel="stylesheet" href="https://fonts.googleapis.com/css2?family=Cinzel:wght@400;600&family=Great+Vibes&family=Lato:wght@400&display=swap">
<style>
:root{
  --board:#5a2a14;
  --paper:#ffffff;
  --ink:#3a3a3a;
  --muted:#8a8a8a;
  --rule:#b9b9b9;
  --band:#c9c9c9;
  --band-light:#ececec;
  --gold:#c9a54a;
  --gold-soft:#e7cf8a;
  --label:#f3e9dc;
}
*{box-sizing:border-box;margin:0;padding:0}
html,body{width:1200px;height:559px;overflow:hidden}
body{background:var(--board);position:relative;font-family:'Lato',sans-serif;color:var(--ink)}
.piece{position:absolute}
.piece-label{position:absolute;top:-14px;left:0;width:100%;text-align:center;font-size:7px;color:var(--label);letter-spacing:.3px}
.sheet{position:absolute;inset:0;background:var(--paper);overflow:hidden;box-shadow:0 2px 6px rgba(0,0,0,.45)}
.brand{position:absolute;display:flex;flex-direction:column;align-items:center;font-family:'Cinzel',serif;font-weight:600;color:var(--ink);line-height:1}
.brand-mark{width:14px;height:14px;border-radius:50%;background:var(--ink);margin-bottom:3px}
.brand-initials{font-size:20px;letter-spacing:1px}
.brand-name{font-size:6.5px;letter-spacing:.6px;margin-top:3px;white-space:nowrap}
.contact{position:absolute;right:22px;top:22px;font-family:'Cinzel',serif;font-size:5px;line-height:7px;color:var(--ink)}
.contact .person{font-size:7px;font-weight:600;margin-bottom:2px}
.falcon-art{position:absolute;background:radial-gradient(ellipse at 50% 45%,#ececec 0%,#f5f5f5 55%,rgba(255,255,255,0) 75%)}
.swoosh{position:absolute;left:0;bottom:0;width:100%}
.tagline{position:absolute;font-family:'Great Vibes',cursive;color:var(--gold);white-space:nowrap}
/* fax */
.fax-title{position:absolute;right:22px;top:70px;font-family:'Cinzel',serif;font-size:10px;font-weight:600}
.fax-table{position:absolute;left:22px;right:22px;top:84px;border-collapse:collapse;font-size:6px;width:333px}
.fax-table td{border:1px solid var(--rule);height:19px;padding:0 4px}
.fax-table td.key{width:34px;color:var(--ink)}
.fax-checks{position:absolute;left:22px;top:176px;display:flex;gap:22px;font-size:5.5px;color:var(--ink)}
.fax-checks span::before{content:"";display:inline-block;width:6px;height:6px;border:1px solid var(--muted);margin-right:3px;vertical-align:-1px}
/* cards */
.card-back{background:linear-gradient(135deg,var(--gold-soft),var(--gold))}
/* envelope back */
.flap{position:absolute;inset:0}
</style>
</head>
<body>

<!-- Fax cover -->
<section class="piece fax-cover" style="left:12px;top:24px;width:377px;height:509px">
  <div class="piece-label">Fax Cover</div>
  <div class="sheet">
    <div class="brand" style="left:22px;top:18px">
      <span class="brand-mark"></span>
      <span class="brand-initials">BRQ</span>
      <span class="brand-name">BRIGHT RIVERS QUALITY</span>
    </div>
    <div class="contact">
      <div class="person">Dale Morrow</div>
      <div>1200 Harbor Lane</div>
      <div>Toms River, NJ 08753</div>
      <div>(732) 555-0148</div>
      <div>dmorrow@br-quality.example</div>
      <div>brightriversquality.example</div>
    </div>
    <div class="fax-title">FAX</div>
    <table class="fax-table">
      <tr><td class="key">To:</td><td></td><td class="key">From:</td><td></td></tr>
      <tr><td class="key">Fax:</td><td></td><td class="key">Pages:</td><td></td></tr>
      <tr><td class="key">Phone:</td><td></td><td class="key">Date:</td><td></td></tr>
      <tr><td class="key">Re:</td><td></td><td class="key">CC:</td><td></td></tr>
    </table>
    <div class="fax-checks">
      <span>Urgent</span><span>For Review</span><span>Please Comment</span><span>Please Reply</span><span>Please Recycle</span>
    </div>
    <div class="falcon-art" role="img" aria-label="Faint falcon illustration" style="left:30px;top:205px;width:180px;height:230px"></div>
    <svg class="swoosh" viewBox="0 0 377 70" height="70" preserveAspectRatio="none">
      <defs><linearGradient id="bandFax" x1="0" y1="0" x2="1" y2="0"><stop offset="0" stop-color="var(--band)"/><stop offset="1" stop-color="var(--band-light)"/></linearGradient></defs>
      <path d="M0 40 C120 10 250 45 377 18 L377 70 L0 70 Z" fill="url(#bandFax)"/>
      <path d="M0 36 C120 6 250 41 377 14" fill="none" stroke="var(--gold)" stroke-width="2"/>
    </svg>
    <div class="tagline" style="right:20px;bottom:10px;font-size:11px">Bringing Nature Indoors</div>
  </div>
</section>

<!-- Letterhead -->
<section class="piece letterhead" style="left:408px;top:24px;width:360px;height:509px">
  <div class="piece-label">Letterhead</div>
  <div class="sheet">
    <div class="brand" style="left:22px;top:18px">
      <span class="brand-mark"></span>
      <span class="brand-initials">BRQ</span>
      <span class="brand-name">BRIGHT RIVERS QUALITY</span>
    </div>
    <div class="contact">
      <div class="person">Dale Morrow</div>
      <div>1200 Harbor Lane</div>
      <div>Toms River, NJ 08753</div>
      <div>(732) 555-0148</div>
      <div>dmorrow@br-quality.example</div>
      <div>brightriversquality.example</div>
    </div>
    <div class="falcon-art" role="img" aria-label="Faint falcon illustration" style="left:40px;top:90px;width:150px;height:260px"></div>
    <svg class="swoosh" viewBox="0 0 360 70" height="70" preserveAspectRatio="none">
      <defs><linearGradient id="bandLetter" x1="0" y1="0" x2="1" y2="0"><stop offset="0" stop-color="var(--band)"/><stop offset="1" stop-color="var(--band-light)"/></linearGradient></defs>
      <path d="M0 40 C110 10 240 45 360 18 L360 70 L0 70 Z" fill="url(#bandLetter)"/>
      <path d="M0 36 C110 6 240 41 360 14" fill="none" stroke="var(--gold)" stroke-width="2"/>
    </svg>
    <div class="tagline" style="right:20px;bottom:10px;font-size:11px">Bringing Nature Indoors</div>
  </div>
</section>

<!-- Business card front -->
<section class="piece card-front" style="left:787px;top:24px;width:154px;height:89px">
  <div class="piece-label">Business Card (Front)</div>
  <div class="sheet">
    <div class="brand" style="left:8px;top:8px">
      <span class="brand-mark" style="width:9px;height:9px;margin-bottom:2px"></span>
      <span class="brand-initials" style="font-size:12px">BRQ</span>
      <span class="brand-name" style="font-size:4px;margin-top:2px">BRIGHT RIVERS QUALITY</span>
    </div>
    <div class="contact" style="right:8px;top:10px;font-size:3.6px;line-height:5px">
      <div class="person" style="font-size:5px">Dale Morrow</div>
      <div>1200 Harbor Lane</div>
      <div>Toms River, NJ 08753</div>
      <div>(732) 555-0148</div>
      <div>dmorrow@br-quality.example</div>
    </div>
    <svg class="swoosh" viewBox="0 0 154 26" height="26" preserveAspectRatio="none">
      <path d="M0 16 C50 4 100 18 154 6 L154 26 L0 26 Z" fill="var(--band)"/>
      <path d="M0 14 C50 2 100 16 154 4" fill="none" stroke="var(--gold)" stroke-width="1.2"/>
    </svg>
    <div class="tagline" style="right:6px;bottom:3px;font-size:6px">Bringing Nature Indoors</div>
  </div>
</section>

<!-- Business card back -->
<section class="piece" style="left:953px;top:24px;width:156px;height:89px">
  <div class="piece-label">Business Card (Back)</div>
  <div class="sheet card-back">
    <div class="tagline" style="left:0;right:0;top:36px;text-align:center;font-size:13px;color:var(--paper)">Bringing Nature Indoors</div>
  </div>
</section>

<!-- Envelope front -->
<section class="piece envelope-front" style="left:782px;top:161px;width:399px;height:158px">
  <div class="piece-label">Envelope (Front)</div>
  <div class="sheet">
    <div class="brand" style="left:14px;top:10px;align-items:flex-start">
      <span class="brand-mark" style="width:11px;height:11px"></span>
      <span class="brand-initials" style="font-size:15px">BRQ</span>
      <span class="brand-name" style="font-size:5px">BRIGHT RIVERS QUALITY</span>
    </div>
    <div style="position:absolute;left:14px;top:58px;font-family:'Cinzel',serif;font-size:4.5px;line-height:6px">
      <div>1200 Harbor Lane</div>
      <div>Toms River, NJ 08753</div>
    </div>
    <svg class="swoosh" viewBox="0 0 399 40" height="40" preserveAspectRatio="none">
      <defs><linearGradient id="bandEnv" x1="0" y1="0" x2="1" y2="0"><stop offset="0" stop-color="var(--band)"/><stop offset="1" stop-color="var(--band-light)"/></linearGradient></defs>
      <path d="M0 24 C130 4 270 28 399 8 L399 40 L0 40 Z" fill="url(#bandEnv)"/>
      <path d="M0 21 C130 1 270 25 399 5" fill="none" stroke="var(--gold)" stroke-width="1.6"/>
    </svg>
    <div class="tagline" style="right:14px;bottom:6px;font-size:9px">Bringing Nature Indoors</div>
  </div>
</section>

<!-- Envelope back -->
<section class="piece envelope-back" style="left:782px;top:348px;width:399px;height:175px">
  <div class="piece-label">Envelope (Back)</div>
  <div class="sheet">
    <svg class="flap" viewBox="0 0 399 175" preserveAspectRatio="none">
      <path d="M0 0 L199.5 95 L399 0" fill="none" stroke="var(--rule)" stroke-width="1"/>
      <path d="M0 175 L160 80 M399 175 L239 80" fill="none" stroke="var(--band-light)" stroke-width="1"/>
    </svg>
    <div class="brand" style="left:176px;top:14px">
      <span class="brand-mark" style="width:9px;height:9px;margin-bottom:2px"></span>
      <span class="brand-initials" style="font-size:12px">BRQ</span>
      <span class="brand-name" style="font-size:4px;margin-top:2px">BRIGHT RIVERS QUALITY</span>
    </div>
  </div>
</section>

</body>
</html>
```